Brochure Design Project: Creative and Bold design for a professional denal appliance cleaner

We are a dental lab that makes teeth night gaurds, teeth retainers, sport mouth guards and teeth whitening trays. This brochure is for a dental appliance cleaner for all these appliances in addition to dentures. The dental appliance cleaner is a strong professional cleaner used by many dentists. Our target market are not dentists, we are selling this as a consumer goods product. The Brand name of the dental appliance cleaner is BRISK VESTA tm. It is unique in that it is a professional cleaner that cleans, disinfects(kills germs), and eliminates ordor. The design of the brochure should communicate a bold and strong cleaner but also have a contemporary creative look to the design.

Requirements
Must have
• -The BRISK VESTA tm Branding and logo on each page.

-ORDER NOW! Order form(credit card/check/money order) on last page on the inside. **PLEASE SEE ATTACHED ORDER FORM: THIS BROCHURE WILL REPLACE THIS BASIC ORDER FORM. The Brochure should be an informational brochure and an ordering brochure. Also this brochure will include a free sample packet of the actual product(maybe best placed on the middle page. The sample will be adhered to the brochure and will need a 3.5''(Height x 2.5''(Width) blank space for the sample. Please refer again to the attached word document to get the idea of the purpose of the brochure.

-Website on the brochure: www.briskvestarinse.example (will be redoing this website next)

-Bullet point features of product:
-Dentist Recommended for proper care of removable dental appliances.
-Dental Appliance DISINFECTANT(Kills Germs) and CLEANER!
-Deep cleans and removes tough stains.
-Eliminates odor from dental appliances.

-Our promise... BRISK VESTA tm professional dental appliance cleaner will clean, disinfect and eliminate odor better then any other cleaner on the market.

-100% SATISFACTION GUARANTEE!

```html
<!DOCTYPE html>
<html lang="en">
<head>
<meta charset="utf-8">
<title>Brisk Vesta Trifold Brochure</title>
<link rel="stylesheet" href="https://fonts.googleapis.com/css2?family=Open+Sans:wght@400;600;700;800&family=PT+Serif:wght@400;700&display=swap">
<style>
:root{
  --ink:#1d3f63;
  --navy:#14578f;
  --blue:#1f74b8;
  --mid:#2f8fd0;
  --sky:#6cc0ea;
  --pale:#dcedf8;
  --paper:#f4f6f8;
  --panel:#e9edf1;
  --white:#ffffff;
  --grape:#7458a6;
  --stage:#eceef0;
  --skin:#d89a86;
}
*{margin:0;padding:0;box-sizing:border-box}
html,body{width:1018px;height:1200px;overflow:hidden;background:var(--stage)}
body{font-family:"Open Sans",Arial,sans-serif;color:var(--ink);position:relative}
.spread{position:absolute;left:44px;width:930px;height:560px;background:var(--white);box-shadow:0 6px 18px rgba(0,0,0,.12);display:flex;overflow:hidden}
.spread--outside{top:24px}
.spread--inside{top:616px}
.panel{position:relative;width:310px;height:100%;overflow:hidden}
.panel + .panel{border-left:1px solid rgba(0,0,0,.06)}
.shapes{position:absolute;inset:0;width:100%;height:100%}
.brand{display:flex;align-items:center;gap:6px;font-weight:700;font-size:13px;letter-spacing:.5px;color:var(--navy)}
.brand__dot{width:10px;height:10px;border-radius:50%;background:var(--navy)}
.brand--light{color:var(--white)}
.brand--light .brand__dot{background:var(--white)}

/* order form */
.order-form{background:var(--paper);padding:26px 22px 20px 24px;font-family:"PT Serif",Georgia,serif;font-size:10.5px;line-height:1.45;color:#2a2a2a}
.order-form p{margin-bottom:9px}
.order-form .caps{text-transform:uppercase}
.order-form .opts{list-style:none;margin-bottom:9px}
.order-form .box{display:inline-block;width:8px;height:8px;border:1px solid #555;margin-right:5px;vertical-align:-1px}
.order-form .cards{display:grid;grid-template-columns:1fr 1fr;gap:2px 8px;list-style:none;margin-bottom:9px;font-size:9.5px;text-transform:uppercase}
.order-form .field{display:flex;gap:6px}
.order-form .line{flex:1;border-bottom:1px solid #999}
.order-form .email{color:var(--blue);font-weight:700}

/* mailing panel */
.mailer{background:var(--paper)}
.mailer__block{position:absolute;left:155px;top:280px;width:420px;transform:translate(-50%,-50%) rotate(90deg);text-align:center}
.mailer__brand{justify-content:center;margin-bottom:60px;font-size:15px}
.mailer__company{font-weight:700;font-size:12px;color:var(--navy)}
.mailer__contact{font-weight:700;font-size:11px;color:var(--navy);line-height:1.35}
.mailer__web{margin-top:34px;font-weight:700;font-size:11px;letter-spacing:3px;color:var(--navy)}

/* cover */
.cover__photo{position:absolute;left:0;top:0;width:310px;height:190px;background:radial-gradient(ellipse at 45% 55%,#fff 0 18%,var(--skin) 40%,#b56f5d 70%,#f1f1f1 100%)}
.cover__tag{position:absolute;right:0;top:156px;width:210px;padding:8px 12px 8px 16px;background:var(--sky);color:var(--white);font-weight:800;font-size:12px;line-height:1.2;text-transform:uppercase}
.cover__tag span{display:block;font-size:15px}
.cover__claims{position:absolute;left:120px;top:290px;list-style:none;color:var(--white);font-weight:700;font-size:12px;line-height:1.9;text-transform:uppercase}
.cover__claims li::before{content:"";display:inline-block;border-left:6px solid var(--white);border-top:4px solid transparent;border-bottom:4px solid transparent;margin-right:7px}
.cover__brand{position:absolute;left:60px;top:440px}

/* inside left */
.intro{background:var(--navy)}
.intro__photo{position:absolute;left:28px;top:54px;width:220px;height:150px;border-radius:50%/40%;background:radial-gradient(ellipse at center,#ffffff 0 30%,#cfe3f1 60%,rgba(31,116,184,0) 75%)}
.intro__label{position:absolute;left:50px;top:262px;padding:5px 12px;background:var(--sky);color:var(--white);font-weight:700;font-size:15px;border:1px solid var(--white)}
.intro__text{position:absolute;left:50px;top:306px;width:235px;color:var(--white);font-family:"PT Serif",Georgia,serif;font-size:11.5px;line-height:1.55}
.intro__brand{position:absolute;left:50px;top:500px}

/* inside middle */
.benefits{background:var(--panel)}
.benefits__title{position:absolute;left:22px;top:46px;font-family:"PT Serif",Georgia,serif;font-size:26px;color:var(--white)}
.benefits__list{position:absolute;left:26px;top:108px;width:262px;list-style:none;font-size:10.5px;line-height:1.4;color:var(--blue)}
.benefits__list li{position:relative;padding-left:13px;margin-bottom:7px}
.benefits__list li::before{content:"";position:absolute;left:0;top:4px;width:6px;height:6px;background:var(--sky)}
.sample{position:absolute;left:75px;top:286px;width:160px;height:224px;background:linear-gradient(160deg,#e8f4fb,#9fd0ee 55%,#5aa9dc);border:1px dashed #8fb6d3}

/* inside right */
.promise{background:var(--white)}
.promise__title{position:absolute;left:18px;top:40px;font-weight:700;font-size:14px;color:var(--white)}
.promise__text{position:absolute;left:18px;top:64px;width:270px;font-size:10px;line-height:1.4;color:var(--white)}
.promise__badge{position:absolute;left:46px;top:150px;width:46px;height:46px;border-radius:50%;background:var(--mid);box-shadow:0 0 0 3px var(--pale)}
.promise__points{position:absolute;left:46px;top:210px;width:220px;font-size:10.5px;line-height:1.35;color:var(--blue);text-transform:uppercase}
.promise__points p{margin-bottom:14px}
.order-now{position:absolute;left:218px;top:378px;width:70px;height:70px;border-radius:50%;background:var(--grape);box-shadow:0 0 0 3px #c9bbe2;display:flex;align-items:center;justify-content:center;text-align:center;color:var(--white);font-weight:800;font-size:13px;line-height:1.1}
.promise__brand{position:absolute;left:110px;top:440px}
</style>
</head>
<body>

<section class="spread spread--outside" aria-label="Brochure outside">
  <div class="panel order-form">
    <p class="caps">Please check box(es) for quantity of Brisk Vesta dental cleaner and disinfectant you wish to order:</p>
    <ul class="opts">
      <li><span class="box"></span>3 Month Supply: $16.99</li>
      <li><span class="box"></span>6 Month Supply: $29.99</li>
      <li><span class="box"></span>12 Month Supply(BEST VALUE!): $39.99</li>
    </ul>
    <p class="field caps">Order total: <span class="line"></span></p>
    <p><span class="caps">Please return order form with teeth impression(s) or mail directly to:</span><br>Bright Harbor Dental LLC<br>1287 Alder Lane<br>Millbrook, WI 53000</p>
    <p class="caps">Payment options:<br>Credit card:</p>
    <ul class="cards">
      <li><span class="box"></span>Northpay</li>
      <li><span class="box"></span>Orbit Card</li>
      <li><span class="box"></span>Meridian</li>
      <li><span class="box"></span>Summit Express</li>
    </ul>
    <p class="field">First Name: <span class="line"></span> Last Name: <span class="line"></span></p>
    <p class="field">Credit Card #: <span class="line"></span> Expiration Date: <span class="line"></span></p>
    <p class="field">Billing Address: <span class="line"></span></p>
    <p class="field">Shipping Address: <span class="line"></span></p>
    <p><span class="box"></span>Check if same as billing address.</p>
    <p><span class="caps">Personal check/bank check/money order:</span><br>Please make Payable To: Bright Harbor Dental LLC</p>
    <p>For customer inquiries, contact:<br><span class="email">sales@brightharbordental.example</span></p>
  </div>

  <div class="panel mailer">
    <div class="mailer__block">
      <div class="brand mailer__brand"><span class="brand__dot"></span>BRISK VESTA</div>
      <div class="mailer__company">Bright Harbor Dental Lab and Supply</div>
      <div class="mailer__contact">877-555-0142<br>www.brightharbordental.example<br>www.briskvestarinse.example<br>www.nightguardhub.example</div>
      <div class="mailer__web">www.briskvestarinse.example</div>
    </div>
  </div>

  <div class="panel cover">
    <div class="cover__photo" role="img" aria-label="Close-up photo of a bright, clean smile"></div>
    <svg class="shapes" viewBox="0 0 310 560" preserveAspectRatio="none" aria-hidden="true">
      <path d="M0 215 Q150 175 310 200 L310 560 L0 560 Z" fill="var(--mid)"/>
      <path d="M0 250 Q150 215 310 235 L310 560 L0 560 Z" fill="var(--navy)"/>
      <rect x="95" y="265" width="200" height="110" rx="16" fill="var(--blue)"/>
    </svg>
    <div class="cover__tag">100% satisfaction guarantee!<span>Professional cleaner</span></div>
    <ul class="cover__claims">
      <li>Deep cleans.</li>
      <li>Disinfects.</li>
      <li>Eliminates odor.</li>
    </ul>
    <div class="brand brand--light cover__brand"><span class="brand__dot"></span>BRISK VESTA</div>
  </div>
</section>

<section class="spread spread--inside" aria-label="Brochure inside">
  <div class="panel intro">
    <svg class="shapes" viewBox="0 0 310 560" preserveAspectRatio="none" aria-hidden="true">
      <path d="M0 0 L310 0 L310 22 Q150 40 0 20 Z" fill="var(--sky)"/>
      <path d="M0 545 Q160 520 310 540 L310 560 L0 560 Z" fill="var(--mid)"/>
    </svg>
    <div class="intro__photo" role="img" aria-label="Photo of a clear dental night guard"></div>
    <div class="intro__label">BRISK VESTA</div>
    <p class="intro__text">Is an extra strength prosthetic cleaner and disinfectant which will safely and effectively remove plaque, tartar, calcium, calculus, coffee, tea, tobacco, and iron stains without damaging ortho dental appliances, soft relines, dentures or partials.</p>
    <div class="brand brand--light intro__brand"><span class="brand__dot"></span>BRISK VESTA</div>
  </div>

  <div class="panel benefits">
    <svg class="shapes" viewBox="0 0 310 560" preserveAspectRatio="none" aria-hidden="true">
      <path d="M0 0 L310 0 L310 20 Q150 30 0 60 Z" fill="var(--sky)"/>
      <path d="M0 40 Q150 25 310 30 L310 72 Q150 68 0 90 Z" fill="var(--mid)"/>
      <path d="M0 540 Q160 515 310 530 L310 560 L0 560 Z" fill="var(--sky)"/>
    </svg>
    <h2 class="benefits__title">Benefits</h2>
    <ul class="benefits__list">
      <li>Dental Appliance DISINFECTANT (Kills Germs) and CLEANER!</li>
      <li>Dentist Recommended for proper care and disinfecting of removable dental appliances.</li>
      <li>Deep cleans and removes tough stains such as plaque, calcium, tartar, coffee, tea and tobacco stains!</li>
      <li>Eliminates 99% of GERMS!</li>
      <li>Eliminates odor from dental appliances!</li>
    </ul>
    <div class="sample" role="img" aria-label="Space for the attached free sample packet of concentrated cleaner"></div>
  </div>

  <div class="panel promise">
    <svg class="shapes" viewBox="0 0 310 560" preserveAspectRatio="none" aria-hidden="true">
      <path d="M0 30 Q150 20 310 0 L310 100 Q150 112 0 120 Z" fill="var(--blue)"/>
      <path d="M0 30 Q150 20 310 0 L310 8 Q150 28 0 38 Z" fill="var(--sky)"/>
      <path d="M0 535 Q160 520 310 525 L310 560 L0 560 Z" fill="var(--mid)"/>
    </svg>
    <h2 class="promise__title">Our Promise</h2>
    <p class="promise__text">BRISK VESTA tm professional dental appliance cleaner will clean, disinfect and eliminate odor better then any other cleaner on the market.</p>
    <div class="promise__badge" aria-hidden="true"></div>
    <div class="promise__points">
      <p>Professional strength!</p>
      <p>Dentist recommended for proper care of dental appliances.</p>
      <p>Deep cleans, disinfects, eliminating 99% of germs and eliminates odor!</p>
    </div>
    <div class="order-now">ORDER<br>NOW!</div>
    <div class="brand promise__brand"><span class="brand__dot"></span>BRISK VESTA</div>
  </div>
</section>

</body>
</html>
```